New Business Card Design Project

hello again,
i have an awful year and we were not able to complete our logo plan. we would like to use our #1 logo for business card design process. the primary colors for business card should be white background with orange & black letters. our business is mobil truck cranes. we deliver heavy stuff and unload cargo with crane that is mounted on our trucks.
here is our business card info:
HARBORLINE LIFT HAULERS, INC.
482 WICKHAM AVE
LAWRENCE, NY 11597
OFFICE - 516 430 2291
DIRECT - 1 888 LIFT HAULS
GERALD@HLHAUL.EXAMPLE
PLEASE also try to get our slogan on card .... "Our Loads Keep Climbin"
lastly please also put "24 hour Knuckleboom Service"
you can call me anytime 24/7 to discuss...my cell # is: 516 907 4463
please also list: Gerald Pruitt, President
Target Market(s)
Heavy Construction industry
Industry/Entity Type
heavy construction industry
Contact Information for Business Card
24 Hr Knuckleboom Service

```html
<!DOCTYPE html>
<html lang="en">
<head>
<meta charset="utf-8">
<title>Harborline Lift Haulers – Business Card</title>
<link href="https://fonts.googleapis.com/css2?family=Montserrat:wght@300;400;600;700;800&family=Roboto+Condensed:wght@400;500;700&display=swap" rel="stylesheet">
<style>
  :root {
    --orange: #f47b16;
    --card-dark: #2a2a2a;
    --band-black: #0b0b0b;
    --skyline: #323232;
    --ink: #1a1a1a;
    --white: #ffffff;
    --stage: #d9d7d4;
  }
  * { margin: 0; padding: 0; box-sizing: border-box; }
  html, body { width: 1200px; height: 1200px; overflow: hidden; }
  body { background: var(--stage); position: relative; font-family: "Montserrat", sans-serif; }

  .card {
    position: absolute; left: 243px; width: 702px; height: 400px;
    border-radius: 22px; overflow: hidden;
  }

  /* Front */
  .card--front { top: 170px; background: var(--card-dark); }
  .front__header {
    position: absolute; top: 30px; width: 100%; text-align: center;
    font-family: "Roboto Condensed", sans-serif; font-weight: 500; color: var(--white);
  }
  .front__company { font-size: 41px; letter-spacing: 0.5px; line-height: 1.15; }
  .front__slogan { font-size: 34px; line-height: 1.3; }
  .front__slogan .accent { color: var(--orange); font-family: "Montserrat", sans-serif; font-weight: 700; font-size: 33px; }
  .front__band {
    position: absolute; top: 144px; height: 130px; width: 100%;
    background: var(--band-black); text-align: center; padding-top: 10px;
  }
  .band__hours { color: var(--orange); font-weight: 700; font-size: 52px; line-height: 1.05; }
  .band__service { color: var(--white); font-weight: 600; font-size: 44px; line-height: 1.2; letter-spacing: 0.5px; }
  .front__skyline {
    position: absolute; top: 274px; left: 40px; right: 24px; height: 86px;
    background: linear-gradient(180deg, #3a3a3a, var(--skyline));
  }
  .front__hotline { position: absolute; top: 296px; width: 100%; text-align: center; }
  .hotline__label { color: var(--white); font-weight: 400; font-size: 26px; letter-spacing: 1px; line-height: 1.1; }
  .hotline__number { color: var(--orange); font-weight: 700; font-size: 43px; line-height: 1.15; }

  /* Back */
  .card--back { top: 630px; background: linear-gradient(135deg, #ffffff 0%, #f2f2f2 55%, #dcdcdc 100%); }
  .brand {
    position: absolute; left: 76px; top: 150px; width: 310px;
    display: flex; align-items: center; gap: 14px;
  }
  .brand__dot { width: 34px; height: 34px; border-radius: 50%; background: var(--orange); flex: none; }
  .brand__name { font-weight: 800; font-size: 29px; line-height: 1.1; color: var(--ink); }

  .contact { position: absolute; left: 424px; top: 128px; font-family: "Roboto Condensed", sans-serif; color: var(--ink); }
  .contact__person { border-left: 3px solid var(--orange); padding-left: 10px; }
  .contact__name { font-size: 25px; font-weight: 500; line-height: 1.05; }
  .contact__title { font-size: 18px; font-weight: 400; line-height: 1.1; }
  .contact__row { display: flex; gap: 12px; align-items: flex-start; font-size: 17px; font-weight: 500; line-height: 1.25; }
  .contact__row svg { flex: none; margin-top: 2px; }
  .contact__address { margin-top: 26px; }
  .contact__phone { margin-top: 24px; }
  .contact__email { margin-top: 2px; }
</style>
</head>
<body>

<section class="card card--front">
  <div class="front__skyline" role="img" aria-label="Faint city skyline illustration"></div>
  <div class="front__header">
    <div class="front__company">HARBORLINE LIFT HAULERS, INC.</div>
    <div class="front__slogan">OUR LOADS KEEP <span class="accent">“CLIMBIN”</span></div>
  </div>
  <div class="front__band">
    <div class="band__hours">24 HOUR</div>
    <div class="band__service">KNUCKLEBOOM SERVICE</div>
  </div>
  <div class="front__hotline">
    <div class="hotline__label">HOTLINE</div>
    <div class="hotline__number">1 888 LIFT HAULS</div>
  </div>
</section>

<section class="card card--back">
  <div class="brand">
    <span class="brand__dot"></span>
    <span class="brand__name">HARBORLINE LIFT HAULERS INC</span>
  </div>

  <div class="contact">
    <div class="contact__person">
      <div class="contact__name">GERALD PRUITT</div>
      <div class="contact__title">PRESIDENT</div>
    </div>

    <div class="contact__row contact__address">
      <svg width="16" height="26" viewBox="0 0 16 26" aria-hidden="true">
        <path d="M8 1a7 7 0 0 0-7 7c0 5 7 12 7 12s7-7 7-12a7 7 0 0 0-7-7z" fill="none" stroke="var(--orange)" stroke-width="2"/>
        <circle cx="8" cy="8" r="2.6" fill="var(--orange)"/>
        <rect x="1" y="24" width="14" height="2" fill="var(--orange)"/>
      </svg>
      <div>482 WICKHAM AVE<br>LAWRENCE, NY 11597</div>
    </div>

    <div class="contact__row contact__phone">
      <svg width="16" height="16" viewBox="0 0 16 16" aria-hidden="true">
        <circle cx="8" cy="8" r="8" fill="var(--orange)"/>
        <path d="M5.2 4.2l1.4 1.6-.8 1.1c.5 1.1 1.3 1.9 2.3 2.4l1.1-.8 1.6 1.4-.9 1.3C7.4 11.1 4.9 8.6 4 5.1z" fill="var(--white)"/>
      </svg>
      <div>516 430 2291</div>
    </div>

    <div class="contact__row contact__email">
      <svg width="16" height="16" viewBox="0 0 16 16" aria-hidden="true">
        <circle cx="8" cy="8" r="8" fill="var(--orange)"/>
        <rect x="4" y="5.2" width="8" height="5.6" rx="0.6" fill="none" stroke="var(--white)" stroke-width="1.2"/>
        <path d="M4.3 5.6L8 8.4l3.7-2.8" fill="none" stroke="var(--white)" stroke-width="1.2"/>
      </svg>
      <div>GERALD@HLHAUL.EXAMPLE</div>
    </div>
  </div>
</section>

</body>
</html>
```